Velvet Afterhours Poster Design

Need poster design made up in next few days, can guarantee payment to winner. Poster must contain the following but feel free to word it better:
Velvet Afterhours
Presented by quenmor Sound
Select resident djs
Drink specials all night
Open from 8pm to 12pm
Find us on Chatterbox
At Larkfield Suites every Saturday
These will be on posters and fliers
Of a3 and roughly a5 size.
Our target audience is people 18-25
We want the posters to be exciting and professional. We would like a blue or purple with black color scheme but there is plenty of room for creative license so have a play around with what you think looks good. We currently don't have a logo but if your including one we would like to see it as m4 as in marble as an element. Our first drink special is cocktails in jars but is not essential to include, can provide proper copy of the picture if you want to include it in your design. Please contact us if you need more information. we will be quick to pick a winner so payment will be provided fast!!!
Thank you all in advance for your submissions!!

```html
<!DOCTYPE html>
<html lang="en">
<head>
<meta charset="utf-8">
<title>Velvet Afterhours Poster</title>
<link rel="stylesheet" href="https://fonts.googleapis.com/css2?family=Gloria+Hallelujah&family=Roboto:wght@400&display=swap">
<style>
  :root {
    --night: #000000;
    --beam: #f0be14;
    --beam-deep: #1a1200;
    --ink: #000000;
    --chalk: #ffffff;
  }
  html, body {
    margin: 0;
    padding: 0;
    width: 1200px;
    height: 900px;
    overflow: hidden;
    background: var(--night);
  }
  .poster {
    display: block;
    width: 1200px;
    height: 900px;
  }
  .hand {
    font-family: "Gloria Hallelujah", cursive;
  }
  .sans {
    font-family: "Roboto", Arial, sans-serif;
    font-weight: 400;
  }
  .brand-mark { fill: var(--beam); font-size: 190px; }
  .event-title { fill: var(--beam); font-size: 74px; }
  .presenter-line { fill: var(--ink); font-size: 68px; }
  .presenter-name { fill: var(--chalk); font-size: 78px; }
  .presenter-tag { fill: var(--chalk); font-size: 42px; }
  .feature { fill: var(--ink); font-size: 46px; }
  .hours { fill: var(--chalk); font-size: 40px; text-transform: uppercase; }
  .footer-note { fill: var(--chalk); font-size: 19px; text-transform: uppercase; }
  .leader { stroke: var(--ink); stroke-width: 7; stroke-linecap: round; }
</style>
</head>
<body>
<svg class="poster" viewBox="0 0 1200 900" xmlns="http://www.w3.org/2000/svg" aria-label="Velvet Afterhours poster">
  <defs>
    <linearGradient id="beam-fade" x1="700" y1="480" x2="1220" y2="880" gradientUnits="userSpaceOnUse">
      <stop offset="0" stop-color="var(--beam)"/>
      <stop offset="0.35" stop-color="#d9a90f"/>
      <stop offset="1" stop-color="var(--beam-deep)"/>
    </linearGradient>
  </defs>

  <rect class="backdrop" width="1200" height="900" fill="var(--night)"/>

  <polygon class="spotlight-beam" points="150,330 325,145 1200,315 1200,900 575,900" fill="url(#beam-fade)"/>

  <text class="brand-mark hand" x="30" y="240">m4</text>

  <text class="event-title hand" x="290" y="108" textLength="515" lengthAdjust="spacingAndGlyphs">Velvet Afterhours</text>

  <text class="presenter-line hand" x="375" y="205" transform="rotate(11 375 205)" textLength="380" lengthAdjust="spacingAndGlyphs">Presented by</text>

  <g class="presenter" transform="rotate(10 315 280)">
    <text class="presenter-name sans" x="315" y="282" textLength="265" lengthAdjust="spacingAndGlyphs">QUENMOR</text>
    <text class="presenter-tag sans" x="583" y="282" textLength="120" lengthAdjust="spacingAndGlyphs">SOUND</text>
  </g>

  <line class="leader" x1="200" y1="395" x2="318" y2="280"/>
  <line class="leader" x1="295" y1="520" x2="415" y2="400"/>
  <line class="leader" x1="390" y1="640" x2="495" y2="522"/>

  <text class="feature hand" x="410" y="388" transform="rotate(12 410 388)" textLength="395" lengthAdjust="spacingAndGlyphs">Select resident DJ's</text>
  <text class="feature hand" x="490" y="518" transform="rotate(12 490 518)" textLength="500" lengthAdjust="spacingAndGlyphs">Drink specials all night</text>

  <text class="hours hand" x="128" y="362" transform="rotate(53 128 362)" textLength="510" lengthAdjust="spacingAndGlyphs">Open from 8pm to 12pm</text>

  <text class="footer-note hand" x="4" y="860" textLength="254" lengthAdjust="spacingAndGlyphs">At Larkfield Suites every Saturday</text>
  <text class="footer-note hand" x="4" y="892" textLength="210" lengthAdjust="spacingAndGlyphs">Follow us on Chatterbox</text>
</svg>
</body>
</html>
```